Local Directory Ad

We currently have an advertisement in our local directory (see attached). We would like to make it look more appealing.
Dimensions are 110mm H X 175mm W
We would like to keep the same colours and contact details remain the same.
Most of the content can remain the same, Just remove the line Tax effective remote area salary packaging and add in Self Managed Super Funds.We want to change mortgage broking to Mortgage Broking and Loan Structuring.

We want to change the line Local accountants Local Knowledge Local Experience - to something like local knowledge beyond compare or unsurpassed local knowledge but open to suggestions on this.

there are some good designs posted so far. I particulalry like the ones from pulmawick, korbu41, and the last one posted by wexlorunti and PLV. Keep up the good work guys

```html
<!DOCTYPE html>
<html lang="en">
<head>
<meta charset="utf-8">
<title>Spinifex Accounting &amp; Finance – Directory Ad</title>
<link rel="stylesheet" href="https://fonts.googleapis.com/css2?family=Noto+Serif:wght@700&family=Roboto+Condensed:wght@400;700&display=swap">
<style>
  :root {
    --navy-deep: #0f1d33;
    --navy: #1d3557;
    --bronze: #6b5236;
    --charcoal: #2a2a2c;
    --ink: #111111;
    --white: #ffffff;
    --sun: #f7c21a;
    --teal: #5fd6c0;
  }
  html, body { margin: 0; padding: 0; overflow: hidden; background: var(--charcoal); }
  .ad {
    position: relative;
    width: 1200px; height: 755px; overflow: hidden;
    background:
      radial-gradient(ellipse 70% 80% at 90% 70%, rgba(140,100,55,.75), transparent 70%),
      radial-gradient(ellipse 60% 70% at 15% 10%, rgba(40,70,120,.8), transparent 70%),
      linear-gradient(100deg, var(--navy-deep) 0%, var(--navy) 35%, #3a3a3e 65%, var(--bronze) 100%);
    font-family: "Roboto Condensed", "Arial Narrow", sans-serif;
    color: var(--white);
  }
  .lens { position: absolute; inset: 0; }
  .brand {
    position: absolute; left: 50px; top: 40px; margin: 0;
    font-family: "Noto Serif", Georgia, serif; font-weight: 700;
    font-size: 88px; line-height: 84px; letter-spacing: -1px;
    text-shadow: 0 3px 10px rgba(0,0,0,.6);
  }
  .licence { position: absolute; left: 50px; top: 336px; font-size: 25px; margin: 0; }
  .tagline {
    position: absolute; left: 0; top: 406px; width: 576px; height: 168px;
    background: var(--sun); border-radius: 0 84px 84px 0;
    color: var(--ink); box-sizing: border-box; padding: 28px 0 0 50px;
    font-size: 34px; line-height: 37px; text-transform: uppercase; margin: 0;
  }
  .tagline strong { font-weight: 700; }
  .services-title {
    position: absolute; left: 720px; top: 50px; margin: 0; width: 440px;
    color: var(--ink); font-weight: 700; font-size: 33px; line-height: 38px;
  }
  .rule { position: absolute; left: 732px; top: 153px; width: 468px; height: 2px; background: var(--teal); }
  .services {
    position: absolute; left: 726px; top: 176px; margin: 0; padding: 0; list-style: none;
    font-size: 24px; line-height: 30px; color: var(--ink);
  }
  .services li { position: relative; padding-left: 20px; margin-bottom: 17px; }
  .services li::before {
    content: ""; position: absolute; left: 0; top: 9px; width: 11px; height: 11px;
    border-radius: 50%; background: var(--white);
  }
  .services li:last-child { line-height: 31px; }
  .icons { position: absolute; left: 744px; top: 448px; }
  .address, .contact {
    position: absolute; top: 608px; margin: 0; font-style: normal;
    font-size: 22px; line-height: 36px;
  }
  .address { left: 42px; }
  .contact { left: 420px; line-height: 32px; }
  .contact .web { font-weight: 700; font-size: 33px; line-height: 44px; }
  .contact span + span { margin-left: 18px; }
</style>
</head>
<body>
<main class="ad">
  <svg class="lens" width="1200" height="755" role="img" aria-label="Magnifying glass lens over a brushed metal backdrop">
    <defs>
      <radialGradient id="glass" cx="0.5" cy="0.45" r="0.55">
        <stop offset="0" stop-color="#9a9288" stop-opacity=".75"/>
        <stop offset="0.7" stop-color="#6e6a66" stop-opacity=".55"/>
        <stop offset="1" stop-color="#3a3a3c" stop-opacity=".35"/>
      </radialGradient>
    </defs>
    <circle cx="960" cy="230" r="342" fill="url(#glass)"/>
    <circle cx="960" cy="230" r="342" fill="none" stroke="#e8e8e8" stroke-width="5"/>
  </svg>

  <h1 class="brand">Spinifex<br>Accounting<br>&amp; Finance</h1>
  <p class="licence">Australian Credit Licence 402 918</p>

  <p class="tagline"><strong>Local</strong> knowledge beyond<br>compare or unsurpassed<br>local <strong>knowledge</strong></p>

  <h2 class="services-title">We are here for you all year round to assist with...</h2>
  <div class="rule"></div>
  <ul class="services">
    <li>Accounting &amp; Taxation</li>
    <li>Business Advice CST and BAS's</li>
    <li>Mortgage Broking &amp; Loan Structuring</li>
    <li>Bookkeeping</li>
    <li>Self Managed Super Funds for<br>your employees</li>
  </ul>

  <svg class="icons" width="400" height="85" aria-hidden="true">
    <g fill="#ffffff">
      <!-- briefcase -->
      <path d="M34 8 h34 a4 4 0 0 1 4 4 v10 h-7 v-7 h-28 v7 h-7 v-10 a4 4 0 0 1 4 -4z"/>
      <rect x="0" y="24" width="102" height="58" rx="3"/>
      <rect x="44" y="36" width="14" height="16" rx="2" fill="#3a3a3c"/>
    </g>
    <g fill="#ffffff" stroke="#3a3a3c" stroke-width="2">
      <!-- binders -->
      <rect x="140" y="16" width="26" height="66" transform="rotate(-14 153 49)"/>
      <rect x="168" y="6" width="28" height="76"/>
      <rect x="200" y="10" width="28" height="72"/>
      <circle cx="182" cy="52" r="5" fill="#3a3a3c"/>
      <circle cx="214" cy="54" r="5" fill="#3a3a3c"/>
    </g>
    <g fill="#ffffff" stroke="#3a3a3c" stroke-width="2">
      <!-- coin stacks -->
      <rect x="294" y="70" width="48" height="12" rx="6"/>
      <rect x="294" y="58" width="48" height="12" rx="6"/>
      <rect x="294" y="46" width="48" height="12" rx="6"/>
      <rect x="294" y="34" width="48" height="12" rx="6"/>
      <rect x="338" y="70" width="48" height="12" rx="6"/>
      <rect x="338" y="58" width="48" height="12" rx="6"/>
      <rect x="338" y="46" width="48" height="12" rx="6"/>
      <rect x="338" y="34" width="48" height="12" rx="6"/>
      <rect x="338" y="22" width="48" height="12" rx="6"/>
      <rect x="338" y="10" width="48" height="12" rx="6"/>
    </g>
  </svg>

  <address class="address">
    Shop 5 Harbour Arcade<br>
    12 Corbel St. Port Hedland<br>
    PO Box 418 Port Hedland 6721
  </address>
  <p class="contact">
    reception@spxaf.com.au<br>
    <span>Ph: 9140 5582</span><span>Fax: 9140 5583</span><br>
    <span class="web">www.spxaf.com.au</span>
  </p>
</main>
</body>
</html>
```